Quotation and Scripture Design

We are a marketing firm looking for a graphic designer who is gifted in the merging of typestyles, colors, and composition into images suitable for framing in the home or office. The design criteria is quite simple, (1) keep it fresh without looking dated or religious, and (2) push the envelope a little with good, solid graphic design. Phase one will involve building our inventory of original artwork to fifty or more pieces to be marketed online. For phase two in addition to a line of greeting cards, we will also offer art pieces reproduced by laser engravers, CNC routers, chemical etching, and digital printers. For this reason it is necessary that all art files be submitted in a vector format.

Target Market(s)

Professional women and men who appreciate and purchase gallery quality artwork.

Industry/Entity Type

Graphic Designer

Requirements
Must have
• Selection of the designer will be based on their graphic interruption of the following two quotations.
Quotation No. 1 - Romans 8:28
And we know that all things work together for good to those who love God, to those who are called according to His purpose.
Quotation No. 2 -Jeremiah 29:11
For I know the plans I have for you, declares the Lord. Plans to prosper you and not to harm you. Plans to give you hope and a future.
Design one of these two formats to fit a 8" x10" frame, and the other to fit a 12" x 12" frame.
Nice to have
• Rich colors, fresh typestyles . . . please no Times Roman. Bold, creative composition is what we are looking for.
Should not have
• Dated, religious artwork found in the local bible bookstore is a very good example of what we DO NOT want. If it is not something you would purchase for yourself or a friend, more than likely it won't meet our criteria.

```html
<!DOCTYPE html>
<html lang="en">
<head>
<meta charset="UTF-8">
<title>Romans 8:28 — Scripture Print</title>
<link rel="stylesheet" href="https://fonts.googleapis.com/css2?family=Pinyon+Script&family=Source+Sans+3:wght@400&family=Poppins:wght@600&family=Cinzel:wght@400&family=Parisienne&display=swap">
<style>
  :root {
    --paper: #ffffff;
    --ink-reference: #3a3560;
    --ink-plum: #7b2464;
    --ink-sand: #d4b9aa;
    --ink-cocoa: #6e3b2d;
    --ink-rose: #d8808f;
    --ink-orchid: #cc8fbf;
    --ink-mauve: #7c6e8c;
  }
  * { margin: 0; padding: 0; box-sizing: border-box; }
  html, body {
    width: 856px;
    height: 1200px;
    overflow: hidden;
    background: var(--paper);
  }
  .print {
    position: relative;
    width: 856px;
    height: 1200px;
    background: var(--paper);
  }
  .verse-line {
    position: absolute;
    left: 118px;
    white-space: nowrap;
    line-height: 1;
  }
  .verse-reference {
    top: 238px;
    font-family: "Pinyon Script", cursive;
    font-size: 44px;
    color: var(--ink-reference);
  }
  .verse-opening {
    top: 318px;
    font-family: "Source Sans 3", sans-serif;
    font-size: 36px;
    color: var(--ink-plum);
    letter-spacing: -0.2px;
  }
  .verse-emphasis {
    top: 380px;
    font-family: "Poppins", sans-serif;
    font-weight: 600;
    font-size: 60px;
    letter-spacing: -2px;
    color: var(--ink-sand);
  }
  .verse-lovers {
    top: 484px;
    font-family: "Cinzel", serif;
    font-size: 42px;
    color: var(--ink-cocoa);
    display: flex;
    align-items: center;
    gap: 10px;
  }
  .verse-lovers .heart {
    width: 72px;
    height: 60px;
    margin-top: -6px;
  }
  .verse-lovers .heart path { fill: var(--ink-rose); }
  .verse-called {
    top: 556px;
    font-family: "Parisienne", cursive;
    font-size: 58px;
    color: var(--ink-orchid);
  }
  .verse-closing {
    top: 652px;
    font-family: "Source Sans 3", sans-serif;
    font-size: 48px;
    color: var(--ink-mauve);
    letter-spacing: -0.3px;
  }
</style>
</head>
<body>
  <main class="print">
    <p class="verse-line verse-reference">Romans 8:28</p>
    <p class="verse-line verse-opening">And we know that all things work</p>
    <p class="verse-line verse-emphasis">together for good</p>
    <p class="verse-line verse-lovers">
      <span>TO THOSE WHO</span>
      <svg class="heart" viewBox="0 0 72 60" role="img" aria-label="love">
        <path d="M36 58 C26 48 2 36 2 18 C2 8 10 2 19 2 C27 2 33 7 36 13 C39 7 45 2 53 2 C62 2 70 8 70 18 C70 36 46 48 36 58 Z"/>
      </svg>
      <span>GOD,</span>
    </p>
    <p class="verse-line verse-called">to those who are called</p>
    <p class="verse-line verse-closing">according to His purpose.</p>
  </main>
</body>
</html>
```